New Service Brochure for The Larkmere Spa

Hi All! We are looking for a new brochure design- tri-fold, double sided, and full color. We are a certified Clear Spa for men and women in the heart of the Catskill Mountains of upstate New York. Our clients would describe us as laid back luxury with no pretensions and a home away from home vibe. Our font is Avalon. Key colors are black, white and gold. Looking for an inviting, clean, and modern/minimalist spread with a touch of elegance. No orchid imagery, please. I would like our "Clear Spa" logo on cover, too please. Front cover image with with logo and "Clear Spa" Sticker . Bottom of back with contact info. We would prefer massages go on left inside page, facials in middle and right inside, nails on back left, but we are open to new or different layout proposals. Thank you!

Target Market(s)

Men & Women.

Industry/Entity Type

Health And Wellness

Font styles to use
Other font styles liked:
• Avalon is our signature font

Requirements
Must have
• Easy on the eyes.
Nice to have
• Negative space.
Should not have
• No orchids. Busy lines and wild colors.

```html
<!DOCTYPE html>
<html lang="en">
<head>
<meta charset="utf-8">
<title>The Larkmere Spa – Service Brochure</title>
<link href="https://fonts.googleapis.com/css2?family=Montserrat:wght@400;600;700&display=swap" rel="stylesheet">
<style>
:root{
  --gold:#e7b21f;
  --black:#141414;
  --white:#ffffff;
  --paper:#f1f1f1;
  --ink:#333333;
  --red:#d8342b;
}
*{box-sizing:border-box;margin:0;padding:0}
html,body{width:798px;height:1200px;overflow:hidden;background:var(--paper);font-family:"Montserrat",sans-serif;color:var(--ink)}
.sheet{position:absolute;left:47px;width:705px;display:flex;box-shadow:0 2px 8px rgba(0,0,0,.18);background:var(--white)}
.sheet--outside{top:52px;height:515px}
.sheet--inside{top:605px;height:560px}
.panel{position:relative;width:235px;height:100%;overflow:hidden}
.photo{position:absolute;left:0;width:100%}
.wave{position:absolute;left:0;width:100%}
.gold-title{font-weight:700;color:var(--gold);text-transform:uppercase;letter-spacing:.3px}
.body-copy{font-size:9px;line-height:1.35}
.price-row{display:flex;gap:38px;font-size:10px;font-weight:600}
.price-row span:last-child{font-weight:400}

/* name lockup: plain text, one weight, one colour */
.brand{position:absolute;left:0;width:100%;display:flex;align-items:center;justify-content:center;gap:8px}
.brand-name{font-family:"Montserrat",sans-serif;font-weight:600;font-size:17px;letter-spacing:.5px}
.brand-dot{width:10px;height:10px;border-radius:50%;background:var(--gold)}
.strapline{position:absolute;left:0;width:100%;text-align:center;font-size:9px}

/* outside: recovery promo */
.recovery-promo .photo{top:0;height:230px;background:linear-gradient(160deg,#e9dfd6,#cdb5a3 55%,#f4efe9)}
.recovery-promo .dark{position:absolute;left:0;top:220px;width:100%;height:295px;background:var(--black)}
.recovery-promo .wave{top:200px}
.recovery-promo .gold-title{position:absolute;left:20px;top:270px;width:190px;font-size:14px;line-height:1.25}
.recovery-promo .body-copy{position:absolute;left:20px;top:335px;width:190px;color:var(--white)}
.recovery-promo .price-row{position:absolute;left:20px;top:470px;color:var(--white)}

/* outside: contact */
.contact .gold-title{position:absolute;left:0;top:38px;width:100%;text-align:center;font-size:13px}
.contact .intro{position:absolute;left:40px;top:62px;width:155px;text-align:center;font-size:8.5px;line-height:1.4}
.contact .wave{top:140px}
.contact .brand{top:222px;color:var(--black)}
.contact .strapline{top:252px}
.contact .details{position:absolute;left:0;top:305px;width:100%;text-align:center;font-size:9px;line-height:1.4}
.contact .details h3{font-size:12px;letter-spacing:1px;margin-bottom:4px;color:var(--black)}
.contact .dots{position:absolute;left:0;top:440px;width:100%;display:flex;justify-content:center;gap:8px}
.contact .dots span{width:18px;height:18px;border:1.5px solid var(--black);border-radius:50%}

/* outside: cover */
.cover .top{position:absolute;left:0;top:0;width:100%;height:160px;background:var(--black)}
.cover .brand{top:62px;color:var(--white)}
.cover .strapline{top:92px;color:var(--white)}
.cover .wave{top:138px}
.cover .photo{top:165px;height:230px;background:linear-gradient(200deg,#f5eee7,#d8c0ad 50%,#efe3d8)}
.cover .seal{position:absolute;left:125px;top:365px;width:85px;height:85px;border-radius:50%;background:#6f8f5e}

/* inside */
.sheet--inside .panel{background:var(--white)}
.band{position:absolute;left:0;width:100%;height:24px;background:var(--gold);color:var(--white);font-weight:700;font-size:12px;text-transform:uppercase;padding:5px 14px;letter-spacing:.3px}
.section-head{position:absolute;left:0;top:0;width:100%;height:58px;background:var(--black);padding:22px 14px;font-weight:700;font-size:18px;color:var(--gold);text-transform:uppercase}
.copy{position:absolute;left:14px;width:200px}
.prices{position:absolute;left:14px;font-size:10px;line-height:1.4}
.prices div{display:flex;gap:40px;font-weight:600}
.prices div span:last-child{font-weight:400}

.massages .photo{top:320px;height:240px;background:linear-gradient(170deg,#eadfd4,#c7a58a 60%,#e4d3c4);clip-path:polygon(0 12%,100% 0,100% 100%,0 100%)}
.tension .photo{top:305px;height:255px;background:linear-gradient(190deg,#f3ebe3,#d7b89e 55%,#efe2d6);clip-path:polygon(0 0,100% 10%,100% 100%,0 100%)}
.recovery .photo{top:190px;height:370px;background:linear-gradient(180deg,#efe8df,#bfa48b 45%,#e9ddd1)}
.stripes{position:absolute;left:0;top:170px}
</style>
</head>
<body>

<section class="sheet sheet--outside">
  <article class="panel recovery-promo">
    <div class="photo" role="img" aria-label="Woman wrapped in a white towel, relaxing"></div>
    <div class="dark"></div>
    <svg class="wave" width="235" height="60" viewBox="0 0 235 60"><path d="M0 30 C70 -5 150 55 235 15 L235 30 C150 65 70 10 0 45Z" fill="var(--gold)"/></svg>
    <h2 class="gold-title">Pulsewave Rapid Recovery Massage</h2>
    <p class="body-copy">Ideal for runners, cyclists, hikers, skiers &amp; riders. Recover faster and feel better with compression sleeves that flush soreness, relieve tired legs and restore circulation.</p>
    <div class="price-row"><span>$135</span><span>55min</span></div>
  </article>

  <article class="panel contact">
    <h2 class="gold-title">Spa Parties</h2>
    <p class="intro">Perfect for bridal showers, birthday parties and any time you want to host a unique and extraordinary experience.</p>
    <svg class="wave" width="235" height="60" viewBox="0 0 235 60"><path d="M0 10 C80 60 160 0 235 30 L235 40 C160 10 80 70 0 25Z" fill="var(--black)"/><path d="M0 25 C80 70 160 10 235 40 L235 48 C160 20 80 78 0 36Z" fill="var(--gold)"/></svg>
    <div class="brand"><span class="brand-dot"></span><span class="brand-name">The Larkmere Spa</span></div>
    <p class="strapline">a boutique spa for men &amp; women</p>
    <div class="details">
      <h3>LOCATION</h3>
      <p>24 Birchwood Hollow Road<br>Larkmere, NY 12400<br>Just off Main Street</p>
      <p style="margin-top:8px">(555) 014-2287<br>info@thelarkmerespa.com</p>
    </div>
    <div class="dots"><span></span><span></span><span></span></div>
  </article>

  <article class="panel cover">
    <div class="top"></div>
    <div class="brand"><span class="brand-dot"></span><span class="brand-name">The Larkmere Spa</span></div>
    <p class="strapline">a boutique spa for men &amp; women</p>
    <div class="photo" role="img" aria-label="Woman receiving a relaxing facial treatment"></div>
    <svg class="wave" width="235" height="40" viewBox="0 0 235 40"><path d="M0 20 C80 0 150 40 235 8 L235 18 C150 48 80 10 0 30Z" fill="var(--gold)"/></svg>
    <div class="seal" role="img" aria-label="Clear Spa certification seal"></div>
  </article>
</section>

<section class="sheet sheet--inside">
  <article class="panel massages">
    <h2 class="section-head">Massages</h2>
    <h3 class="band" style="top:60px">Swedish Massage</h3>
    <p class="copy body-copy" style="top:94px">Relaxing and therapeutic. Ease tension and enhance circulation. Great for a first time massage or any spa veteran.</p>
    <div class="prices" style="top:145px"><div><span>$100</span><span>55min</span></div><div><span>$160</span><span>90min</span></div></div>
    <h3 class="band" style="top:185px">Deep Tissue</h3>
    <p class="copy body-copy" style="top:219px">A therapeutic combination of slow and deep pressure alleviates chronic pain, muscle fatigue and limited range of motion.</p>
    <div class="prices" style="top:272px"><div><span>$115</span><span>55min</span></div><div><span>$175</span><span>90min</span></div></div>
    <div class="photo" role="img" aria-label="Guest receiving a back massage"></div>
  </article>

  <article class="panel tension">
    <h3 class="band" style="top:0">Tension Tamer</h3>
    <p class="copy body-copy" style="top:34px">Mind, neck and shoulders. Deep focus with hot towels, muscle soothing oils and cupping.</p>
    <div class="prices" style="top:80px"><div><span>$125</span><span>55min</span></div><div><span>$185</span><span>90min</span></div></div>
    <h3 class="band" style="top:130px">Hot Stone</h3>
    <p class="copy body-copy" style="top:164px">Smooth heated stones glide over tired muscles, melting tension deep within the body for the ultimate warm retreat.</p>
    <div class="prices" style="top:225px"><div><span>$175</span><span>90min</span></div></div>
    <div class="photo" role="img" aria-label="Woman relaxing during a massage"></div>
  </article>

  <article class="panel recovery">
    <h3 class="band" style="top:0">Recovery</h3>
    <p class="copy body-copy" style="top:34px">Specific to your athletic needs, whether pre or post workout. Relax, stretch, and recover.</p>
    <div class="prices" style="top:80px"><div><span>$110</span><span>55min</span></div><div><span>$170</span><span>90min</span></div></div>
    <div class="photo" role="img" aria-label="Hot stones placed along a guest's back"></div>
    <svg class="stripes" width="235" height="60" viewBox="0 0 235 60"><path d="M0 40 L235 10" stroke="var(--red)" stroke-width="3"/><path d="M0 48 L235 18" stroke="var(--white)" stroke-width="4"/></svg>
  </article>
</section>

</body>
</html>
```